Drag Show Flyer

We are holding a Drag Show, we are looking for something fun and exciting, over the top is a must.

Show Date: Saturday September 2nd 2017
Venue: Pelican Row Cafe Bunbury
Doors open 7pm
Tickets: $50 per person, includes glass of sparkling on arrival and canapes
Tickets available at the Venue or from ticketloom.com.au

Target Market(s)

Female, Hens Party, LBGT

Industry/Entity Type

Entertainment

Colors

Designer to choose colors to be used in the design.

Requirements
Must have
• Show Date: Saturday September 2nd 2017
• Venue: Pelican Row Cafe Bunbury
• Doors open 7pm
• Tickets: $50 per person, includes glass of sparkling on arrival and canapes
• Tickets available at the Venue or from ticketloom.com.au

```html
<!DOCTYPE html>
<html lang="en">
<head>
<meta charset="utf-8">
<title>Drag Show Flyer</title>
<link rel="stylesheet" href="https://fonts.googleapis.com/css2?family=Abril+Fatface&family=Anton&family=Oswald:wght@300;400;700&family=Libre+Baskerville:ital,wght@0,400;0,700;1,700&display=swap">
<style>
  :root {
    --blue: #1273bd;
    --orange: #f0692b;
    --red: #ec1c24;
    --yellow: #ffe800;
    --white: #ffffff;
    --ink: #111111;
  }
  * { margin: 0; padding: 0; box-sizing: border-box; }
  html, body { width: 848px; height: 1200px; overflow: hidden; }
  body { background: #ffffff; }
  .flyer {
    position: relative;
    width: 848px;
    height: 1200px;
    overflow: hidden;
    background:
      radial-gradient(ellipse 420px 700px at 300px 450px, rgba(245,240,170,0.85), rgba(245,240,170,0) 70%),
      radial-gradient(ellipse 420px 800px at 800px 400px, rgba(255,255,255,0.95), rgba(255,255,255,0) 70%),
      linear-gradient(90deg, #a9d6d9 0%, #dfe7c4 30%, #f4f3d8 55%, #f8fbf8 80%, #e9f4f6 100%);
  }
  .flyer::after {
    content: "";
    position: absolute;
    left: 0; right: 0; bottom: 0; height: 260px;
    background: linear-gradient(180deg, rgba(210,235,238,0) 0%, rgba(200,230,235,0.8) 100%);
    pointer-events: none;
  }
  .headline { font-size: inherit; font-weight: normal; }
  .title-word {
    position: absolute;
    font-family: "Abril Fatface", serif;
    color: var(--blue);
    line-height: 1;
    white-space: nowrap;
    z-index: 1;
    transform-origin: center center;
  }
  .title-drag { left: 48px; top: 80px; font-size: 218px; transform: rotate(-10deg); letter-spacing: -3px; }
  .title-show { left: 240px; top: 200px; font-size: 214px; transform: rotate(-12deg); letter-spacing: -4px; }
  .price-badge { position: absolute; left: 466px; top: 310px; width: 360px; height: 360px; z-index: 2; }
  .price-text {
    position: absolute;
    left: 500px; top: 355px; width: 290px;
    text-align: center;
    transform: rotate(-14deg);
    z-index: 3;
    font-family: "Oswald", sans-serif;
    line-height: 1;
  }
  .price-amount { font-family: "Anton", sans-serif; color: var(--white); font-size: 128px; line-height: 1.05; }
  .price-line { font-size: 26px; font-weight: 300; color: var(--white); }
  .price-highlight { font-size: 30px; font-weight: 700; color: var(--yellow); }
  .doors { position: absolute; left: 190px; top: 492px; text-align: center; z-index: 1; }
  .doors-label { font-family: "Oswald", sans-serif; font-weight: 300; font-size: 34px; color: var(--ink); }
  .doors-time { font-family: "Anton", sans-serif; font-size: 100px; color: var(--ink); line-height: 1.05; }
  .rule { position: absolute; left: 43px; width: 754px; height: 4px; background: var(--orange); z-index: 1; }
  .rule-top { top: 679px; }
  .rule-bottom { top: 787px; }
  .tagline {
    position: absolute; left: 0; width: 848px; top: 678px;
    text-align: center; z-index: 1;
    font-family: "Oswald", sans-serif; font-weight: 700;
    font-size: 94px; line-height: 1.1; color: var(--orange); letter-spacing: -1px;
  }
  .show-date, .venue {
    position: absolute; left: 0; width: 848px; text-align: center; z-index: 1;
    font-family: "Libre Baskerville", serif; font-weight: 700; color: var(--blue);
  }
  .show-date { top: 800px; font-size: 36px; }
  .venue { top: 870px; font-size: 36px; font-style: italic; }
  .ticket-band {
    position: absolute; left: 0; top: 941px; width: 848px; height: 53px;
    background: var(--orange); z-index: 1;
    display: flex; align-items: center; justify-content: center; gap: 10px;
    font-family: "Libre Baskerville", serif; color: var(--ink);
  }
  .ticket-note { font-size: 17px; letter-spacing: 1px; }
  .ticket-url { font-size: 26px; font-weight: 700; }
  .partners {
    position: absolute; left: 0; top: 1020px; width: 848px; height: 130px; z-index: 2;
    display: flex; align-items: center; justify-content: space-around; padding: 0 60px;
    font-family: "Oswald", sans-serif; font-weight: 400; color: var(--ink);
  }
  .partner { display: flex; align-items: center; gap: 12px; font-size: 26px; }
  .partner-mark { flex: none; background: var(--ink); }
  .partner-mark.circle { width: 64px; height: 64px; border-radius: 50%; }
  .partner-mark.square { width: 40px; height: 40px; }
  .footer-strip { position: absolute; left: 0; bottom: 0; width: 848px; height: 20px; background: #000; z-index: 3; }
</style>
</head>
<body>
<main class="flyer">
  <h1 class="headline">
    <span class="title-word title-drag">Drag</span>
    <span class="title-word title-show">Show</span>
  </h1>

  <svg class="price-badge" viewBox="-180 -180 360 360" aria-hidden="true">
    <g fill="var(--red)">
      <rect x="-128" y="-128" width="256" height="256"/>
      <rect x="-128" y="-128" width="256" height="256" transform="rotate(15)"/>
      <rect x="-128" y="-128" width="256" height="256" transform="rotate(30)"/>
      <rect x="-128" y="-128" width="256" height="256" transform="rotate(45)"/>
      <rect x="-128" y="-128" width="256" height="256" transform="rotate(60)"/>
      <rect x="-128" y="-128" width="256" height="256" transform="rotate(75)"/>
    </g>
  </svg>
  <div class="price-text">
    <div class="price-amount">$50</div>
    <div class="price-line">per person,</div>
    <div class="price-line">includes</div>
    <div class="price-highlight">glass of sparkling</div>
    <div class="price-line">on arrival and</div>
    <div class="price-highlight">canapes</div>
  </div>

  <div class="doors">
    <div class="doors-label">Doors open</div>
    <div class="doors-time">7pm</div>
  </div>

  <div class="rule rule-top"></div>
  <p class="tagline">fun and excitement</p>
  <div class="rule rule-bottom"></div>

  <p class="show-date">Saturday, September 2nd, 2017</p>
  <p class="venue">Pelican Row Cafe Bunbury</p>

  <div class="ticket-band">
    <span class="ticket-note">Tickets available at the Venue or from</span>
    <span class="ticket-url">ticketloom.com.au</span>
  </div>

  <div class="partners">
    <div class="partner"><span class="partner-mark square"></span>Pelican Row</div>
    <div class="partner"><span class="partner-mark circle"></span>the lantern group</div>
    <div class="partner"><span class="partner-mark square"></span>Loud Lip Productions</div>
  </div>

  <div class="footer-strip"></div>
</main>
</body>
</html>
```